BrightHarbor is a fund management company that takes just four market positions a year. each position is linked to a big geopolitical and economic event happening in the world. So for example we may be buying gold mining stocks-these are the companies who dig the gold out of the ground, as all the gold is currently being bought by Asia, or buying the japanese stock market as this is one of the big stories of today.

I am looking for a logo that represents 'BrightHarbor'-the Bright Harbor.

I would like it to be small and sit to the left of the name of the company on the left hand side(I think!)on the top line of the business card please.

Industry/Entity Type

Mining

Contact Information for Business Card

BrightHarbor Investment management Ltd
41 Fennick Lane
London E9 7QT

Tomas P Hulme

Mob: 0(44)7839254086
Off: 0(44) 203 xxxx
email: th@brightharbor-fm.example

```html
<!DOCTYPE html>
<html lang="en">
<head>
<meta charset="utf-8">
<title>BrightHarbor Investment Management Ltd – Business Card</title>
<link rel="stylesheet" href="https://fonts.googleapis.com/css2?family=Questrial&display=swap">
<style>
  :root {
    --card-bg: #ffffff;
    --ink: #111111;
    --brand-blue: #2f8ff0;
    --accent-rule: #3a7ee0;
    --divider: #9a9a9a;
  }
  html, body {
    margin: 0;
    padding: 0;
    overflow: hidden;
    background: var(--card-bg);
  }
  .card {
    position: relative;
    width: 1200px;
    height: 702px;
    background: var(--card-bg);
    font-family: "Questrial", "Helvetica Neue", Arial, sans-serif;
    color: var(--ink);
    overflow: hidden;
  }
  .brand-mark {
    position: absolute;
    left: 157px;
    top: 136px;
    width: 104px;
    height: 104px;
  }
  .company-name {
    position: absolute;
    left: 284px;
    top: 146px;
    margin: 0;
    font-weight: 400;
    line-height: 1;
  }
  .company-name .line-one {
    display: block;
    font-size: 40px;
  }
  .company-name .brand-word {
    color: var(--ink);
  }
  .company-name .line-two {
    display: block;
    font-size: 32px;
    margin-top: 12px;
  }
  .contact-block {
    position: absolute;
    left: 580px;
    top: 309px;
    height: 320px;
    border-left: 3px solid var(--accent-rule);
    padding-left: 16px;
  }
  .person-name {
    margin: 16px 0 8px;
    font-size: 38px;
    font-weight: 400;
    line-height: 1.1;
    letter-spacing: 0.3px;
  }
  .contact-lines,
  .address-lines {
    margin: 0;
    font-size: 28px;
    line-height: 39px;
    font-style: normal;
  }
  .divider {
    width: 396px;
    height: 0;
    border: 0;
    border-top: 1px solid var(--divider);
    margin: 9px 0 10px;
  }
</style>
</head>
<body>
  <main class="card">
    <svg class="brand-mark" viewBox="0 0 104 104" aria-hidden="true">
      <circle cx="52" cy="52" r="50" fill="var(--brand-blue)"/>
    </svg>

    <h1 class="company-name">
      <span class="line-one"><span class="brand-word">BrightHarbor</span> Investment</span>
      <span class="line-two">Management Ltd</span>
    </h1>

    <section class="contact-block">
      <h2 class="person-name">Tomas P Hulme</h2>
      <p class="contact-lines">
        Mob: 0(44)7839254086<br>
        Off: 0(44) 203 xxxx<br>
        email: th@brightharbor-fm.example
      </p>
      <hr class="divider">
      <address class="address-lines">
        41 Fennick Lane<br>
        London<br>
        E9 7QT
      </address>
    </section>
  </main>
</body>
</html>
```